Private Security Company Business Card and Logo Design

Looking for a modern conservative business card design for our new private security company Harbor Ridge Guard Co., Inc. or HRGC for short.
Private Security Services. The current logo we have is not very good and honestly would like a sharp logo for the card instead of using the one we have now. Open to ideas. I am easy just looking for something nicer then what I can personally design on cardmillo. I searched on zintoo for Security Company business cards went to images and found some nice designs that were made here.

Target Market(s)

Security Services

Industry/Entity Type

Business

Contact Information for Business Card

Harbor Ridge Guard Co., Inc.
President, cell,office,fax,email, website,
Logo etc, whatever is needed for a standard business card
Can provide personal Information later.

Colors
0556a4
ffffff
474747

Requirements
Must have
• Modern but conservative,
Nice to have
• color choices
• Blue, white, Grey

```html
<!DOCTYPE html>
<html lang="en">
<head>
<meta charset="UTF-8">
<title>Harbor Ridge Guard Co., Inc. — Business Card</title>
<link rel="stylesheet" href="https://fonts.googleapis.com/css2?family=Source+Sans+3:wght@400;600&family=Roboto:wght@700&display=swap">
<style>
  :root {
    --brand-blue: #0556a4;
    --brand-white: #ffffff;
    --brand-grey: #474747;
    --card-black: #050505;
    --card-charcoal: #1c1c1c;
    --stage: #3a3330;
  }
  * { box-sizing: border-box; margin: 0; padding: 0; }
  html, body {
    width: 1200px;
    height: 844px;
    overflow: hidden;
    background: var(--stage);
  }
  .stage {
    position: relative;
    width: 1200px;
    height: 844px;
  }
  .card {
    position: absolute;
    width: 525px;
    height: 300px;
    overflow: hidden;
    box-shadow: 0 14px 30px rgba(0, 0, 0, 0.55);
  }

  /* Contact side */
  .card--contact {
    left: 45px;
    top: 330px;
    background: linear-gradient(100deg, var(--card-black) 0%, var(--card-black) 45%, var(--card-charcoal) 100%);
    font-family: "Source Sans 3", "Myriad Pro", sans-serif;
    color: var(--brand-white);
  }
  .band-top, .band-bottom {
    position: absolute;
    left: 0;
    width: 100%;
    background: var(--brand-blue);
  }
  .band-top { top: 0; height: 9px; }
  .band-bottom { bottom: 0; height: 14px; }
  .person {
    position: absolute;
    top: 56px;
    left: 150px;
    width: 170px;
    text-align: center;
  }
  .person__name {
    font-size: 15px;
    font-weight: 600;
    letter-spacing: 0.3px;
    color: var(--brand-blue);
    text-transform: uppercase;
    padding-bottom: 2px;
    border-bottom: 1px solid var(--brand-blue);
  }
  .person__title {
    font-size: 12.5px;
    margin-top: 3px;
  }
  .contact-list {
    position: absolute;
    left: 0;
    width: 100%;
    top: 156px;
    list-style: none;
    text-align: center;
    font-size: 14px;
    line-height: 18px;
  }
  .contact-list .address { margin-top: 10px; }

  /* Brand side */
  .card--brand {
    left: 630px;
    top: 230px;
    background: radial-gradient(ellipse 55% 60% at 48% 38%, #262626 0%, #0c0c0c 60%, var(--card-black) 100%);
  }
  .tab {
    position: absolute;
    width: 34px;
    height: 26px;
    background: var(--brand-blue);
  }
  .tab--upper { top: 28px; right: 0; border-right: 4px solid #dcdcdc; }
  .tab--lower { top: 152px; left: 0; border-left: 4px solid #dcdcdc; }
  .brand {
    position: absolute;
    top: 58px;
    left: 0;
    width: 100%;
    text-align: center;
    font-family: "Roboto", Arial, sans-serif;
    font-weight: 700;
  }
  .brand__mark {
    display: inline-flex;
    align-items: center;
    gap: 12px;
    color: var(--brand-white);
    font-size: 34px;
  }
  .brand__dot {
    width: 30px;
    height: 30px;
    border-radius: 50%;
    background: var(--brand-blue);
  }
  .brand__name {
    margin-top: 56px;
    font-size: 29px;
    color: var(--brand-blue);
    letter-spacing: 0.2px;
  }
</style>
</head>
<body>
<main class="stage">
  <section class="card card--contact" aria-label="Contact side of business card">
    <div class="band-top"></div>
    <div class="person">
      <h1 class="person__name">Marcus Hale</h1>
      <p class="person__title">Managing Director</p>
    </div>
    <ul class="contact-list">
      <li>041-338-2067</li>
      <li>127-904-5513</li>
      <li>mhale@harborridgeguard.com</li>
      <li>www.hrgcguard.com</li>
      <li class="address">88 Quayside Way Suite 4 | Port Allen, HR | 204518</li>
    </ul>
    <div class="band-bottom"></div>
  </section>

  <section class="card card--brand" aria-label="Brand side of business card">
    <div class="tab tab--upper"></div>
    <div class="tab tab--lower"></div>
    <div class="brand">
      <div class="brand__mark"><span class="brand__dot"></span><span>HRGC</span></div>
      <p class="brand__name">Harbor Ridge Guard</p>
    </div>
  </section>
</main>
</body>
</html>
```